Unique Business Card Design

Unique Business Card design for our orthotic and prosthetic company. Our logo is on our website, color is light blue. Unique shape (artificial leg shaped, vertical, etc..) preferred. Logo, business name, individual name and basic demographics needed.

Industry/Entity Type

Business

Contact Information for Business Card

Logo, Industry, Phone # Logo, "Prosthetic & Orthotic Services" Place to add individual name and contact info

Colors
cee9f5

Requirements
Must have
• The icon must be there, placement of "Prosthetic & Orthotic Services" can be moved
Nice to have
• Like the mix of light blue, and a little darker blue. One design included the icons from my website which was a nice touch

```html
<!DOCTYPE html>
<html lang="en">
<head>
<meta charset="utf-8">
<title>Strideform Inc. – Business Card</title>
<link href="https://fonts.googleapis.com/css2?family=Roboto:wght@400;500&family=Open+Sans:wght@600&family=Cormorant+Garamond:ital,wght@1,500&display=swap" rel="stylesheet">
<style>
  :root {
    --page-bg: #e6e4e0;
    --card-bg: #cfe7f4;
    --brand-blue: #2e3494;
    --faint-circle: #bdd6ec;
    --ink: #1a1a1a;
  }
  * { margin: 0; padding: 0; box-sizing: border-box; }
  html, body {
    width: 900px; height: 1200px; overflow: hidden;
    background: var(--page-bg);
  }
  .card {
    position: absolute; left: 193px; top: 157px;
    width: 517px; height: 884px;
    background: var(--card-bg);
    overflow: hidden;
    box-shadow: 0 6px 18px rgba(0,0,0,0.25);
  }
  .backdrop-circle {
    position: absolute; left: 235px; top: 13px;
    width: 524px; height: 524px; border-radius: 50%;
    background: var(--faint-circle);
  }
  .brand-mark {
    position: absolute; left: 189px; top: 164px;
    width: 144px; height: 144px; border-radius: 50%;
    background: var(--brand-blue);
  }
  .brand-name {
    position: absolute; left: 0; width: 517px; top: 306px;
    text-align: center;
    font-family: 'Open Sans', sans-serif; font-weight: 600;
    font-size: 44px; letter-spacing: 0.5px;
    color: var(--brand-blue);
  }
  .brand-rule {
    position: absolute; left: 65px; top: 365px;
    width: 394px; height: 3px; background: var(--brand-blue);
  }
  .tagline {
    position: absolute; left: 0; width: 524px; top: 374px;
    text-align: center;
    font-family: 'Cormorant Garamond', serif; font-style: italic; font-weight: 500;
    font-size: 28px; color: var(--brand-blue);
  }
  .side-tab {
    position: absolute; top: 543px; width: 23px; height: 296px;
    background: var(--brand-blue);
  }
  .side-tab--left { left: 0; border-radius: 0 23px 23px 0; }
  .side-tab--right { right: 0; border-radius: 23px 0 0 23px; }
  .contact {
    position: absolute; left: 65px; top: 562px;
    font-family: 'Roboto', sans-serif; color: var(--ink);
  }
  .contact__name { font-size: 24px; font-weight: 500; }
  .contact__credentials { color: var(--brand-blue); }
  .contact__address { margin-top: 14px; font-size: 18px; line-height: 27px; }
  .contact__list { list-style: none; margin-top: 14px; font-size: 18px; line-height: 27px; }
  .contact__list li { display: flex; align-items: center; }
  .contact__icon { width: 15px; height: 15px; margin-right: 8px; fill: var(--brand-blue); }
</style>
</head>
<body>
<div class="card">
  <div class="backdrop-circle" aria-hidden="true"></div>

  <div class="brand-mark" aria-hidden="true"></div>
  <div class="brand-name">STRIDEFORM INC.</div>
  <div class="brand-rule"></div>
  <div class="tagline">Prosthetic &amp; Orthotic Services</div>

  <div class="side-tab side-tab--left"></div>
  <div class="side-tab side-tab--right"></div>

  <div class="contact">
    <div class="contact__name">Mira Kalston, <span class="contact__credentials">CO LPO</span></div>
    <div class="contact__address">2280 Harbor Ave<br>Brookvale, NY 11500</div>
    <ul class="contact__list">
      <li><svg class="contact__icon" viewBox="0 0 16 16"><path d="M4 0h8a1.5 1.5 0 0 1 1.5 1.5v13A1.5 1.5 0 0 1 12 16H4a1.5 1.5 0 0 1-1.5-1.5v-13A1.5 1.5 0 0 1 4 0zm0 2v10h8V2zm4 11a1 1 0 1 0 0 2 1 1 0 0 0 0-2z"/></svg>555-0142871</li>
      <li><svg class="contact__icon" viewBox="0 0 16 16"><path d="M3.6 1l2.4 3-1.4 1.8c.9 2 2.6 3.7 4.6 4.6L11 9l3 2.4-1.3 2.8C7 14.3 1.7 9 1.8 2.3z"/></svg>555-310-2400</li>
      <li><svg class="contact__icon" viewBox="0 0 16 16"><path d="M4 1h8v4H4zM2 6h12a1.5 1.5 0 0 1 1.5 1.5V12H13v3H3v-3H.5V7.5A1.5 1.5 0 0 1 2 6zm3 5v3h6v-3z"/></svg>555-310-2491</li>
      <li><svg class="contact__icon" viewBox="0 0 16 16"><path d="M1 3h14v1L8 9 1 4zm0 2.5l7 5 7-5V13H1z"/></svg>Mkalston@strideforminc.com</li>
      <li><svg class="contact__icon" viewBox="0 0 16 16"><path d="M1 2h14v9H1zm1.5 1.5v6h11v-6zM6 12h4v1.5h2V15H4v-1.5h2z"/></svg>www.strideforminc.com</li>
    </ul>
  </div>
</div>
</body>
</html>
```